Electric mountain bike tours nz

We are an Electric Mountain bike tour company in New Zealand. We will be offering bike rental and guided tours around the Nelson region in New Zealand. I want our website to represent both Mountain biking and New Zealand with the colours layout and features. We want tabs for the following:
-1 about us
-2 what we offer
-3 bookings/contact
Under the about us tab will be who we are as a a company. I want the ability to add videos to each of these tabs as we move foward with videos of the tracks we will be riding. I want the website to be editable so I can add and remove videos/photos myself. Also "our bikes" will be under this tab.
Under the what we offer tab will be
-1 bike rental and pricing
-2 guided tours and pricing
-3 recommended package deals.
I want to able to put the tracks under the guided tours tab and select beginner/ intermediate/advanced and have the tracks in each of the following to match the rider level. Also to be able to have a small video of the track would be great in this section.
Bookings and contact tab
(Further information for this tab to be updated soon)
Coded - Design and coding required
1 page
- Silver ferns, kiwi, mountains

```html
<!DOCTYPE html>
<html lang="en">
<head>
<meta charset="utf-8">
<title>KORUTRAX – Electric Mountain Bike Tours NZ</title>
<link href="https://fonts.googleapis.com/css2?family=Lato:ital,wght@0,400;0,700;0,900;1,700;1,900&family=Roboto:wght@400;500;700&display=swap" rel="stylesheet">
<style>
:root{
  --green:#1f7a2f;
  --green-bright:#2e9a3f;
  --green-deep:#17652a;
  --dark:#1e1e1e;
  --darker:#141414;
  --orange:#f47b2a;
  --orange-deep:#e8621c;
  --blue:#2e5fc4;
  --blue-deep:#2349a6;
  --white:#ffffff;
  --grey:#6f6f6f;
  --light:#f2f2f2;
  --faint:#ececec;
}
*{box-sizing:border-box;margin:0;padding:0}
html,body{width:1200px;height:4534px;overflow:hidden}
body{position:relative;font-family:'Roboto',sans-serif;color:var(--dark);background:var(--white)}
.abs{position:absolute}
.heading{font-family:'Lato',sans-serif;font-weight:900;font-style:italic;text-transform:uppercase}
.btn{position:absolute;display:flex;align-items:center;justify-content:center;gap:8px;height:46px;border-radius:23px;font-family:'Lato',sans-serif;font-weight:900;font-size:15px;text-transform:uppercase;letter-spacing:.3px}
.btn-green{background:var(--green);color:var(--white)}
.btn-white{background:var(--white);color:var(--dark)}
.btn-outline{background:var(--white);color:var(--dark);border:2px solid var(--dark)}
.btn svg{width:14px;height:14px}

/* header / hero */
.hero{position:absolute;left:0;top:0;width:1200px;height:705px}
.hero-photo{position:absolute;inset:0;background:linear-gradient(180deg,#5d7fa3 0%,#9db3c6 30%,#5a5d52 62%,#2a2a22 100%)}
.hero-shade{position:absolute;inset:0;background:linear-gradient(90deg,rgba(0,0,0,.15),rgba(0,0,0,.35))}
.topbar{position:absolute;left:0;top:0;width:1200px;height:110px;background:rgba(20,20,20,.55)}
.brand{position:absolute;left:120px;top:22px;display:flex;align-items:center;gap:12px}
.brand-dot{width:34px;height:34px;border-radius:50%;background:var(--white)}
.brand-name{font-family:'Lato',sans-serif;font-weight:900;font-size:34px;color:var(--white);letter-spacing:1px}
.nav{position:absolute;right:100px;top:60px;display:flex;gap:36px;font-family:'Lato',sans-serif;font-weight:900;font-size:15px;color:var(--white)}
.hero-title{left:615px;top:365px;font-size:46px;color:var(--white)}
.hero-text{left:615px;top:440px;width:500px;font-size:19px;line-height:30px;color:var(--white)}
.hero-arrow{position:absolute;top:402px;width:20px;height:20px}

/* welcome */
.ghost{position:absolute;font-family:'Lato',sans-serif;font-weight:900;font-style:italic;text-transform:uppercase;color:var(--faint);white-space:nowrap}
.section-title{position:absolute;left:0;width:1200px;text-align:center;font-size:34px;color:var(--darker)}
.intro{position:absolute;left:280px;width:640px;text-align:center;font-size:13px;line-height:22px;color:var(--grey)}
.card{position:absolute;top:921px;width:314px;height:296px;background:var(--white);box-shadow:0 2px 8px rgba(0,0,0,.25)}
.card-photo{height:220px}
.card-caption{padding:18px 20px 0;font-family:'Lato',sans-serif;font-weight:700;font-size:17px;line-height:28px;color:#555}

/* split */
.split{position:absolute;left:0;top:1344px;width:1200px;height:489px}
.split-left{position:absolute;left:0;top:0;width:600px;height:489px;background:linear-gradient(135deg,#3c3a35,#1d1c1a);clip-path:polygon(0 0,100% 6%,100% 100%,0 80%)}
.split-right{position:absolute;left:600px;top:0;width:600px;height:489px;background:linear-gradient(135deg,#2f8f3c,#1b6b2a);clip-path:polygon(0 6%,100% 0,100% 80%,0 100%)}
.split-title{font-size:30px;color:var(--white)}
.split-text{width:410px;font-size:13px;line-height:22px;color:#e6e6e6}

/* packages */
.tabs{position:absolute;top:1924px;left:0;width:1200px;display:flex;justify-content:center;gap:14px;font-family:'Lato',sans-serif;font-weight:900;font-size:12px}
.tab{padding:6px 12px;color:var(--dark)}
.tab.active{background:var(--dark);color:var(--white)}
.plan{position:absolute;background:var(--dark);color:var(--white);text-align:center}
.plan-head{font-size:26px;color:var(--white);height:50px;line-height:50px}
.plan-price{height:114px;display:flex;align-items:center;justify-content:center;gap:4px;font-family:'Lato',sans-serif;color:var(--white)}
.plan-price sup{font-size:26px;font-weight:900;align-self:flex-start;margin-top:26px}
.plan-price strong{font-size:62px;font-weight:900;font-style:italic}
.plan-price small{font-size:13px;align-self:flex-end;margin-bottom:34px}
.plan-name{margin-top:32px;font-size:20px;color:#e0e0e0}
.plan-list{list-style:none;margin-top:20px;font-size:14px;color:#dcdcdc}
.plan-list li{height:51px;line-height:51px}
.plan .btn{position:relative;margin:12px auto 0;width:120px;height:40px;font-size:14px}

/* banner */
.banner{position:absolute;left:0;top:2818px;width:1200px;height:398px;background:linear-gradient(180deg,#3e4a3c 0%,#5a5648 50%,#2b2a24 100%)}
.banner-title{position:absolute;left:0;top:112px;width:1200px;text-align:center;font-size:38px;line-height:52px;color:var(--white)}

/* about */
.about-title{left:100px;top:3300px;font-size:34px;color:var(--darker)}
.about-text{left:100px;width:530px;font-size:13px;line-height:22px;color:var(--grey)}
.video-frame{left:725px;top:3313px;width:423px;height:266px;border:3px solid var(--green)}
.video{left:688px;top:3355px;width:408px;height:263px;background:linear-gradient(160deg,#5c6e3c,#7a5a36 60%,#3c3a2a)}

/* testimonials */
.testi-bg{position:absolute;left:0;top:3715px;width:1200px;height:437px;background:linear-gradient(180deg,#ffffff,#f1f1ee)}
.divider{position:absolute;left:100px;top:3715px;width:1000px;height:1px;background:#d0d0d0}
.testi{position:absolute;top:3860px;width:310px}
.avatar{position:absolute;left:0;top:10px;width:60px;height:60px;border-radius:50%;background:#c9b8a4;border:3px solid var(--white);box-shadow:0 0 0 2px var(--green)}
.stars{position:absolute;left:78px;top:0;display:flex;gap:2px}
.stars svg{width:13px;height:13px}
.quote{position:absolute;left:78px;top:22px;width:232px;font-size:12px;line-height:18px;font-style:italic;color:#666}
.who{position:absolute;left:0;top:136px;font-size:12px;color:#333}
.who strong{display:block;font-weight:500}
.who span{color:#777}
.dots{position:absolute;left:582px;top:4072px;display:flex;gap:6px}
.dots i{width:10px;height:10px;border-radius:50%;border:1px solid #555}
.dots i.on{background:#555}

/* footer */
.footer{position:absolute;left:0;top:4152px;width:1200px;height:382px;background:linear-gradient(180deg,#262626,#171717)}
.footer-col-title{font-family:'Lato',sans-serif;font-weight:900;font-size:17px;color:var(--white);text-transform:uppercase}
.links{list-style:none;font-size:13px;color:#ddd}
.links li{height:29px;display:flex;align-items:center;gap:10px}
.links li::before{content:"";width:6px;height:6px;border-right:2px solid #ddd;border-top:2px solid #ddd;transform:rotate(45deg)}
.social{display:flex;gap:14px}
.social i{width:20px;height:20px;border-radius:50%;background:var(--white)}
.copyright{position:absolute;left:0;top:4482px;width:1200px;text-align:center;font-size:13px;color:#ccc}
</style>
</head>
<body>

<!-- HERO -->
<header class="hero">
  <div class="hero-photo" role="img" aria-label="Group of riders with electric mountain bikes raising their arms at sunset on a hilltop"></div>
  <div class="hero-shade"></div>
  <div class="topbar"></div>
  <div class="brand"><span class="brand-dot"></span><span class="brand-name">KORUTRAX</span></div>
  <nav class="nav"><span>HOME</span><span>ABOUT US</span><span>WHAT WE OFFER</span><span>BOOKINGS</span><span>CONTACT US</span></nav>
  <svg class="hero-arrow" style="left:40px" viewBox="0 0 20 20"><path d="M13 3 6 10l7 7" fill="none" stroke="#fff" stroke-width="2.5"/></svg>
  <svg class="hero-arrow" style="right:40px" viewBox="0 0 20 20"><path d="M7 3l7 7-7 7" fill="none" stroke="#fff" stroke-width="2.5"/></svg>
  <h1 class="abs heading hero-title">Electric Bike Tours</h1>
  <p class="abs hero-text">Nemo enim ipsam voluptatem quia voluptas sit aspernatur aut odit aut fugit, sed quia consequuntur magni.</p>
  <a class="btn btn-green" style="left:618px;top:530px;width:170px">Read More
    <svg viewBox="0 0 14 14"><circle cx="7" cy="7" r="7" fill="#fff"/><path d="M5.5 4l3 3-3 3" fill="none" stroke="#1f7a2f" stroke-width="1.8"/></svg></a>
</header>

<!-- WELCOME -->
<section>
  <div class="ghost" style="left:0;width:1200px;text-align:center;top:742px;font-size:78px">Welcome to Korutrax</div>
  <h2 class="section-title heading" style="top:768px">Welcome to Korutrax</h2>
  <p class="intro" style="top:838px">At vero eos et accusamus et iusto odio dignissimos ducimus qui blanditiis praesentium voluptatum deleniti atque corrupti quos dolores et quas molestias excepturi sint occaecati cupiditate.</p>
  <div class="card" style="left:100px"><div class="card-photo" role="img" aria-label="Riders resting beside their bikes on a trail" style="background:linear-gradient(160deg,#6f8f5a,#8a7a5c)"></div><p class="card-caption">The Summer Tours Feet Cycling City Name, NZ</p></div>
  <div class="card" style="left:444px"><div class="card-photo" role="img" aria-label="Electric mountain bike on a light studio background" style="background:linear-gradient(160deg,#e4e4e4,#c9c9c9)"></div><p class="card-caption">The Summer Tours Feet Cycling City Name, NZ</p></div>
  <div class="card" style="left:788px"><div class="card-photo" role="img" aria-label="Rider on a mountain ridge with lake and peaks behind" style="background:linear-gradient(180deg,#7fa2c6,#5e6b52 60%,#3d3a2c)"></div><p class="card-caption">The Summer Tours Feet Cycling City Name, NZ</p></div>
  <a class="btn btn-green" style="left:405px;top:1267px;width:188px">Book Your Bike</a>
  <a class="btn btn-outline" style="left:607px;top:1267px;width:188px">Download Guide</a>
</section>

<!-- RENTAL / GUIDE SPLIT -->
<section class="split">
  <div class="split-left" role="img" aria-label="Row of rental mountain bikes parked against a building"></div>
  <div class="split-right" role="img" aria-label="Green tinted photo of a rider on a forest track"></div>
  <h3 class="abs heading split-title" style="left:100px;top:122px">Bike Rental</h3>
  <p class="abs split-text" style="left:100px;top:182px">At vero eos et accusamus et iusto odio dignissimos ducimus qui blanditiis praesentium voluptatum deleniti atque corrupti quos dolores et quas molestias excepturi sint occaecati cupiditate non provident, similique sunt in culpa qui officia deserunt.</p>
  <a class="btn btn-green" style="left:100px;top:309px;width:150px">Book Now
    <svg viewBox="0 0 14 14"><circle cx="7" cy="7" r="7" fill="#fff"/><path d="M5.5 4l3 3-3 3" fill="none" stroke="#1f7a2f" stroke-width="1.8"/></svg></a>
  <h3 class="abs heading split-title" style="left:700px;top:122px">Tours Guide</h3>
  <p class="abs split-text" style="left:700px;top:182px">At vero eos et accusamus et iusto odio dignissimos ducimus qui blanditiis praesentium voluptatum deleniti atque corrupti quos dolores et quas molestias excepturi sint occaecati cupiditate non provident, similique sunt in culpa qui officia deserunt.</p>
  <a class="btn btn-white" style="left:700px;top:309px;width:150px">Download
    <svg viewBox="0 0 14 14"><circle cx="7" cy="7" r="7" fill="#1e1e1e"/><path d="M5.5 4l3 3-3 3" fill="none" stroke="#fff" stroke-width="1.8"/></svg></a>
</section>

<!-- PACKAGES -->
<section>
  <div class="ghost" style="left:0;width:1200px;text-align:center;top:1832px;font-size:78px">Our Packages</div>
  <h2 class="section-title heading" style="top:1858px">Our Packages</h2>
  <div class="tabs"><span class="tab">BIKE RENTAL</span><span class="tab">GUIDED TOURS</span><span class="tab active">RECOMMENDED</span></div>

  <div class="plan" style="left:100px;top:2041px;width:332px;height:611px">
    <div class="plan-head heading" style="background:var(--orange-deep)">Starter</div>
    <div class="plan-price" style="background:var(--orange)"><sup>$</sup><strong>19</strong><small>/ MONTH</small></div>
    <p class="plan-name heading" style="font-weight:700">Single Place Travel</p>
    <ul class="plan-list"><li>Lorem ipsum dolorel</li><li>At vero eos et accusamus</li><li>Nam libero tempore coluta</li><li>Excepteur sint occaecat</li><li>On the other had esounce</li></ul>
    <a class="btn btn-green">Book Now</a>
  </div>

  <div class="plan" style="left:432px;top:2005px;width:332px;height:683px;z-index:2">
    <div class="plan-head heading" style="background:var(--green-deep);height:56px;line-height:56px">Standard</div>
    <div class="plan-price" style="background:var(--green-bright);height:144px"><sup>$</sup><strong>39</strong><small>/ MONTH</small></div>
    <p class="plan-name heading" style="font-weight:700;margin-top:28px">Three Place Travel</p>
    <ul class="plan-list"><li>Nam libero tempore coluta</li><li>On the other had esounce</li><li>Lorem ipsum dolorel</li><li>At vero eos et accusamus</li><li>Excepteur sint occaecat</li></ul>
    <a class="btn btn-green">Book Now</a>
  </div>

  <div class="plan" style="left:764px;top:2041px;width:336px;height:611px">
    <div class="plan-head heading" style="background:var(--blue-deep)">Ultimate</div>
    <div class="plan-price" style="background:var(--blue)"><sup>$</sup><strong>59</strong><small>/ MONTH</small></div>
    <p class="plan-name heading" style="font-weight:700">Five Place Travel</p>
    <ul class="plan-list"><li>Excepteur sint occaecat</li><li>Nam libero tempore coluta</li><li>At vero eos et accusamus</li><li>On the other had esounce</li><li>Lorem ipsum dolorel</li></ul>
    <a class="btn btn-green">Book Now</a>
  </div>
</section>

<!-- BOOKING BANNER -->
<section class="banner" role="img" aria-label="Electric mountain bike parked beside a road sign in the bush">
  <h2 class="banner-title heading">Book Your Electric Bike Tours<br>in New Zealand</h2>
  <a class="btn btn-green" style="left:520px;top:236px;width:160px">Book Now
    <svg viewBox="0 0 14 14"><circle cx="7" cy="7" r="7" fill="#fff"/><path d="M5.5 4l3 3-3 3" fill="none" stroke="#1f7a2f" stroke-width="1.8"/></svg></a>
</section>

<!-- ABOUT -->
<section>
  <div class="ghost" style="left:-60px;top:3420px;font-size:90px;transform:rotate(-90deg);transform-origin:center;color:#f0f0f0">About Us</div>
  <h2 class="abs heading about-title">Travel Further and Faster</h2>
  <p class="abs about-text" style="top:3362px">Sed ut perspiciatis unde omnis iste natus error sit voluptatem accusantium doloremque lau-dantium, totam rem aperiam, eaque ipsa quae ab illo.</p>
  <p class="abs about-text" style="top:3434px">Inventore veritatis et quasi architecto beatae vitae dicta sunt explicabo. Nemo enim ipsam voluptatem quia voluptas sit aspernatur aut odit aut fugit, sed quia consequuntur magni dolores eos qui ratione voluptatem sequi nesciunt. Neque porro quisquam est, qui dolorem ipsum quia dolor sit amet, consectetur, adipisci velit.</p>
  <a class="btn btn-green" style="left:100px;top:3575px;width:160px">Read More
    <svg viewBox="0 0 14 14"><circle cx="7" cy="7" r="7" fill="#fff"/><path d="M5.5 4l3 3-3 3" fill="none" stroke="#1f7a2f" stroke-width="1.8"/></svg></a>
  <div class="abs video-frame"></div>
  <div class="abs video" role="img" aria-label="Video still of an electric mountain bike beside a trail signpost">
    <svg class="abs" style="left:174px;top:102px" width="60" height="60" viewBox="0 0 60 60"><circle cx="30" cy="30" r="30" fill="#1e1e1e"/><path d="M24 18l18 12-18 12z" fill="#fff"/></svg>
  </div>
</section>

<!-- TESTIMONIALS -->
<section>
  <div class="testi-bg" role="img" aria-label="Faded photo of a rider on a forest trail"></div>
  <div class="divider"></div>
  <h2 class="section-title heading" style="top:3782px">Testimonials</h2>
  <svg class="abs" style="left:26px;top:3972px" width="16" height="16" viewBox="0 0 16 16"><path d="M11 2 5 8l6 6" fill="none" stroke="#555" stroke-width="2"/></svg>
  <svg class="abs" style="left:1160px;top:3972px" width="16" height="16" viewBox="0 0 16 16"><path d="M5 2l6 6-6 6" fill="none" stroke="#555" stroke-width="2"/></svg>

  <div class="testi" style="left:100px">
    <div class="avatar" role="img" aria-label="Customer portrait"></div>
    <div class="stars"><svg viewBox="0 0 20 20"><path d="M10 1l2.8 6 6.2.6-4.7 4.2 1.4 6.2L10 14.8 4.3 18l1.4-6.2L1 7.6 7.2 7z" fill="#f0a81e"/></svg><svg viewBox="0 0 20 20"><path d="M10 1l2.8 6 6.2.6-4.7 4.2 1.4 6.2L10 14.8 4.3 18l1.4-6.2L1 7.6 7.2 7z" fill="#f0a81e"/></svg><svg viewBox="0 0 20 20"><path d="M10 1l2.8 6 6.2.6-4.7 4.2 1.4 6.2L10 14.8 4.3 18l1.4-6.2L1 7.6 7.2 7z" fill="#f0a81e"/></svg><svg viewBox="0 0 20 20"><path d="M10 1l2.8 6 6.2.6-4.7 4.2 1.4 6.2L10 14.8 4.3 18l1.4-6.2L1 7.6 7.2 7z" fill="#f0a81e"/></svg><svg viewBox="0 0 20 20"><path d="M10 1l2.8 6 6.2.6-4.7 4.2 1.4 6.2L10 14.8 4.3 18l1.4-6.2L1 7.6 7.2 7z" fill="#ccc"/></svg></div>
    <p class="quote">“ At vero eos et accusamus et iustodio dignissimos ducimus qui blanditpraesent ium voluptatum deleniti atque corrupti quos dolores quas molestias ”</p>
    <p class="who"><strong>MARA QUINN</strong><span>Creative Manager, NZ</span></p>
  </div>
  <div class="testi" style="left:444px">
    <div class="avatar" role="img" aria-label="Customer portrait"></div>
    <div class="stars"><svg viewBox="0 0 20 20"><path d="M10 1l2.8 6 6.2.6-4.7 4.2 1.4 6.2L10 14.8 4.3 18l1.4-6.2L1 7.6 7.2 7z" fill="#f0a81e"/></svg><svg viewBox="0 0 20 20"><path d="M10 1l2.8 6 6.2.6-4.7 4.2 1.4 6.2L10 14.8 4.3 18l1.4-6.2L1 7.6 7.2 7z" fill="#f0a81e"/></svg><svg viewBox="0 0 20 20"><path d="M10 1l2.8 6 6.2.6-4.7 4.2 1.4 6.2L10 14.8 4.3 18l1.4-6.2L1 7.6 7.2 7z" fill="#f0a81e"/></svg><svg viewBox="0 0 20 20"><path d="M10 1l2.8 6 6.2.6-4.7 4.2 1.4 6.2L10 14.8 4.3 18l1.4-6.2L1 7.6 7.2 7z" fill="#f0a81e"/></svg><svg viewBox="0 0 20 20"><path d="M10 1l2.8 6 6.2.6-4.7 4.2 1.4 6.2L10 14.8 4.3 18l1.4-6.2L1 7.6 7.2 7z" fill="#ccc"/></svg></div>
    <p class="quote">“ At vero eos et accusamus et iustodio dignissimos ducimus qui blanditpraesent ium voluptatum deleniti atque corrupti quos dolores quas molestias ”</p>
    <p class="who"><strong>TOMAS REED</strong><span>Events Manager, NZ</span></p>
  </div>
  <div class="testi" style="left:791px">
    <div class="avatar" role="img" aria-label="Customer portrait"></div>
    <div class="stars"><svg viewBox="0 0 20 20"><path d="M10 1l2.8 6 6.2.6-4.7 4.2 1.4 6.2L10 14.8 4.3 18l1.4-6.2L1 7.6 7.2 7z" fill="#f0a81e"/></svg><svg viewBox="0 0 20 20"><path d="M10 1l2.8 6 6.2.6-4.7 4.2 1.4 6.2L10 14.8 4.3 18l1.4-6.2L1 7.6 7.2 7z" fill="#f0a81e"/></svg><svg viewBox="0 0 20 20"><path d="M10 1l2.8 6 6.2.6-4.7 4.2 1.4 6.2L10 14.8 4.3 18l1.4-6.2L1 7.6 7.2 7z" fill="#f0a81e"/></svg><svg viewBox="0 0 20 20"><path d="M10 1l2.8 6 6.2.6-4.7 4.2 1.4 6.2L10 14.8 4.3 18l1.4-6.2L1 7.6 7.2 7z" fill="#f0a81e"/></svg><svg viewBox="0 0 20 20"><path d="M10 1l2.8 6 6.2.6-4.7 4.2 1.4 6.2L10 14.8 4.3 18l1.4-6.2L1 7.6 7.2 7z" fill="#ccc"/></svg></div>
    <p class="quote">“ At vero eos et accusamus et iustodio dignissimos ducimus qui blanditpraesent ium voluptatum deleniti atque corrupti quos dolores quas molestias ”</p>
    <p class="who"><strong>LENA HART</strong><span>Sports Manager, NZ</span></p>
  </div>
  <div class="dots"><i></i><i class="on"></i><i></i></div>
</section>

<!-- FOOTER -->
<footer class="footer" role="img" aria-label="Dark photo of a rider at dusk behind the footer">
  <div class="abs" style="left:136px;top:110px;display:flex;align-items:center;gap:10px"><span class="brand-dot" style="width:28px;height:28px"></span><span class="brand-name" style="font-size:28px">KORUTRAX</span></div>
  <div class="abs social" style="left:100px;top:224px"><i></i><i></i><i></i><i></i><i></i></div>

  <h4 class="abs footer-col-title" style="left:414px;top:76px">Quick Links</h4>
  <ul class="abs links" style="left:420px;top:114px"><li>Home</li><li>About Us</li><li>What We Offer</li><li>Tour Guide</li><li>Contact Us</li></ul>
  <ul class="abs links" style="left:590px;top:114px"><li>Info</li><li>Blog Post</li><li>Press</li><li>Privacy Policy</li><li>Terms of Service</li></ul>

  <h4 class="abs footer-col-title" style="left:828px;top:76px">Newsletter Subscription</h4>
  <p class="abs" style="left:828px;top:114px;width:260px;font-size:13px;line-height:21px;color:#ddd">Register your Email Address to get a more information about us</p>
  <div class="abs" style="left:828px;top:170px;width:272px;height:36px;background:var(--white);font-size:13px;color:#999;padding:9px 12px">Email</div>
  <a class="btn btn-green" style="left:828px;top:220px;width:106px;height:34px;font-size:13px">Subscribe</a>

  <div class="abs" style="left:100px;top:296px;width:1000px;height:1px;background:#555"></div>
</footer>
<p class="copyright">Copyrights © 2018 KORUTRAX. All Rights Reserved.</p>

</body>
</html>
```